Startup company business card (Media & Advertising)

we need a business card design for a company that is a startup in the media and aggregation industry. Card needs to look funky and of a new breed/modern and upmarket.

Target Market(s)

advertisers/ brand agencies & media publishers

Industry/Entity Type

Advertising

Contact Information for Business Card

Please ensure the front face signifies our brand (plumvexo.com) and back has details for the contact. Standard contact such as phone , address, email , website etc.

Font styles to use
Other font styles liked:
• use styleguide and logo font and color

Colors

Designer to choose colors to be used in the design.

Requirements
Must have
• We are disrupting the media and agency industry so subtlety would be good to use imagery to signify this
Nice to have
• Please use logo colors for branding
Should not have
• be as creative and provide few options. Pick a brand color from logo and styleguide

```html
<!DOCTYPE html>
<html lang="en">
<head>
<meta charset="utf-8">
<title>plumvexo business card</title>
<link rel="stylesheet" href="https://fonts.googleapis.com/css2?family=Nunito:wght@900&family=Nunito+Sans:wght@400;600;800&display=swap">
<style>
  :root {
    --brand-red: #e33340;
    --card-white: #f8f8f8;
    --ink: #1c1c1c;
    --page-bg: #e9e6e1;
    --headline-white: #f4f4f4;
  }
  * { box-sizing: border-box; margin: 0; padding: 0; }
  html, body {
    width: 900px;
    height: 1200px;
    overflow: hidden;
    background: var(--page-bg);
  }
  .canvas {
    position: relative;
    width: 900px;
    height: 1200px;
  }
  .card {
    position: absolute;
    left: 75px;
    width: 768px;
    border-radius: 18px;
    overflow: hidden;
    box-shadow: 0 4px 14px rgba(0, 0, 0, 0.18);
  }
  /* Front face */
  .card-front {
    top: 133px;
    height: 438px;
    background: var(--brand-red);
  }
  .headline {
    position: absolute;
    left: -63px;
    top: 37px;
    width: 900px;
    height: 300px;
    transform: rotate(-20deg);
    transform-origin: center;
    text-align: center;
    font-family: "Nunito", sans-serif;
    font-weight: 900;
    font-size: 86px;
    line-height: 100px;
    color: var(--headline-white);
    letter-spacing: 0.5px;
    white-space: nowrap;
  }
  .cursor-large {
    position: absolute;
    left: 630px;
    top: 300px;
    width: 96px;
    height: 96px;
  }
  /* Back face */
  .card-back {
    top: 627px;
    height: 440px;
    background: var(--card-white);
    font-family: "Nunito Sans", sans-serif;
    color: var(--ink);
  }
  .contact-name {
    position: absolute;
    left: 55px;
    top: 42px;
    font-size: 27px;
    font-weight: 400;
  }
  .cursor-small {
    position: absolute;
    left: 164px;
    top: 66px;
    width: 24px;
    height: 24px;
  }
  .contact-role {
    position: absolute;
    right: 55px;
    top: 38px;
    font-size: 25px;
    font-weight: 400;
  }
  .brand {
    position: absolute;
    left: 0;
    right: 0;
    top: 180px;
    display: flex;
    justify-content: center;
    align-items: center;
    gap: 18px;
  }
  .brand-dot {
    width: 62px;
    height: 62px;
    border-radius: 50%;
    background: var(--brand-red);
  }
  .brand-name {
    font-size: 52px;
    font-weight: 800;
    color: var(--ink);
    letter-spacing: 0.5px;
  }
  .contact-line {
    position: absolute;
    left: 55px;
    right: 55px;
    bottom: 32px;
    display: flex;
    justify-content: space-between;
    font-size: 22px;
    font-weight: 400;
  }
</style>
</head>
<body>
<main class="canvas">
  <section class="card card-front" aria-label="Card front">
    <h1 class="headline">Publish your<br>advertisement in<br>just a few clicks</h1>
    <svg class="cursor-large" viewBox="0 0 96 96" aria-hidden="true">
      <polygon points="2,2 2,82 24,62 46,94 66,82 46,52 76,50" fill="var(--headline-white)"/>
    </svg>
  </section>

  <section class="card card-back" aria-label="Card back">
    <p class="contact-name">Johnathan Doe</p>
    <svg class="cursor-small" viewBox="0 0 24 24" aria-hidden="true">
      <polygon points="1,1 1,19 6,14 11,23 15,21 10,12 18,12" fill="var(--brand-red)"/>
    </svg>
    <p class="contact-role">Director</p>
    <div class="brand">
      <span class="brand-dot" aria-hidden="true"></span>
      <span class="brand-name">plumvexo</span>
    </div>
    <p class="contact-line">
      <span>012 345 6489</span><span>|</span><span>email@domain.com</span><span>|</span><span>www.plumvexo.com</span>
    </p>
  </section>
</main>
</body>
</html>
```